Fast-casual chicken restaurant Plume Rally needs a catering menu design

We need a catering menu designed for Plume Rally. We are looking to design a 24x36in landscape menu board for our new catering menu. The catering memo attached includes our catering menu and Plume Rally branding. More information about our brand can be found at https://plumerally.example/.

```html
<!DOCTYPE html>
<html lang="en">
<head>
<meta charset="utf-8">
<title>Plume Rally Catering Menu</title>
<link href="https://fonts.googleapis.com/css2?family=Montserrat:wght@400;500;800;900&display=swap" rel="stylesheet">
<style>
:root{
  --slate:#5b6889;
  --red:#d83a2b;
  --yellow:#fdd230;
  --ink:#5a5a5a;
  --white:#ffffff;
}
*{margin:0;padding:0;box-sizing:border-box}
html,body{width:1200px;height:800px;overflow:hidden;background:var(--white)}
body{font-family:"Montserrat",sans-serif;color:var(--ink)}
.menu{position:relative;width:1200px;height:800px;overflow:hidden}
.abs{position:absolute}
.hero-photo{left:0;top:0;width:704px;height:315px;background:radial-gradient(ellipse at 40% 40%,#c5662c,#9c5a33 55%,#6e3f22)}
.section-head{position:absolute;height:58px;color:var(--white);font-weight:900;font-size:23px;letter-spacing:.3px;display:flex;align-items:center;justify-content:center}
.section-head.slate{background:var(--slate)}
.section-head.red{background:var(--red)}
.rule-red{position:absolute;background:var(--red)}
.rule-slate{position:absolute;background:var(--slate)}
.tab{position:absolute;background:var(--yellow);border-radius:0 0 40px 40px;display:flex;flex-direction:column;align-items:center;text-align:center}
.tab-top{font-size:13px;font-weight:500;margin-top:16px;line-height:1.3}
.cal{position:absolute;left:50%;bottom:4px;transform:translateX(-50%);border:2px solid var(--white);border-radius:50%;display:flex;flex-direction:column;align-items:center;justify-content:center;font-size:14px;line-height:1.2;font-weight:500}
.deal-title{position:absolute;font-weight:900;font-size:26px;color:var(--ink);line-height:1}
.deal-text{position:absolute;font-size:22px;line-height:27px;font-weight:500}
.price{position:absolute;color:var(--red);font-weight:900;font-size:26px;line-height:1;white-space:nowrap}
.price sup{font-size:14px;vertical-align:8px;margin-right:2px}
.item-title{position:absolute;z-index:2;font-weight:900;font-size:23px;line-height:23px;color:var(--ink)}
.item-price{position:absolute;z-index:2;color:var(--red);font-weight:900;font-size:22px;line-height:1;text-align:right}
.item-price sup{font-size:12px;vertical-align:7px;margin-right:2px}
.size{position:absolute;font-size:16px;font-weight:500;letter-spacing:.3px}
.photo{position:absolute;z-index:1;border-radius:8px}
.cup{position:absolute;background:linear-gradient(90deg,#b8161a,#e0312b 60%,#b8161a);border-radius:4px 4px 10px 10px}
.flavors{position:absolute;left:712px;top:575px;width:481px;border-collapse:collapse;font-size:13px;line-height:16px}
.flavors th{background:var(--red);color:var(--white);font-weight:500;font-size:16px;height:33px;text-align:center}
.flavors td{height:33px;padding:0 8px;vertical-align:middle;border-left:2px solid var(--slate)}
.flavors td:first-child{border-left:none}
.flavors tr.hl td{background:var(--yellow)}
.cup-size{position:absolute;font-size:16px;font-weight:500}
</style>
</head>
<body>
<main class="menu">
  <div class="abs hero-photo" role="img" aria-label="Spread of wings, tenders, onion rings, waffle fries and dipping sauces on a wooden table"></div>

  <div class="section-head slate" style="left:0;top:273px;width:287px">PACKAGED DEALS</div>
  <div class="section-head red" style="left:351px;top:273px;width:287px">PER PERSON DEALS</div>
  <div class="section-head slate" style="left:704px;top:0;width:287px;height:59px;font-size:24px">A LA CARTE</div>

  <!-- packaged deals -->
  <div class="tab" style="left:9px;top:331px;width:70px;height:114px"><div class="tab-top">4 PAX</div><div class="cal" style="width:62px;height:62px">0,000<span>CAL</span></div></div>
  <div class="deal-title" style="left:91px;top:342px">FAMILY</div>
  <div class="deal-text" style="left:91px;top:372px">12 tenders, sauces,<br>dressing, large side<br>2L</div>
  <div class="price" style="left:242px;top:438px"><sup>$</sup>24.99</div>

  <div class="rule-red" style="left:9px;top:467px;width:663px;height:2px"></div>
  <div class="tab" style="left:9px;top:469px;width:70px;height:118px"><div class="tab-top">10 PAX</div><div class="cal" style="width:62px;height:62px">0,000<span>CAL</span></div></div>
  <div class="deal-title" style="left:91px;top:486px">TAILGATE</div>
  <div class="deal-text" style="left:91px;top:515px">20 tenders, 30 wings,<br>sauces, dressings, 2L<br>1 party side</div>
  <div class="price" style="left:242px;top:582px"><sup>$</sup>75.99</div>

  <div class="rule-red" style="left:9px;top:611px;width:663px;height:2px"></div>
  <div class="tab" style="left:9px;top:613px;width:70px;height:120px"><div class="tab-top">10 PAX</div><div class="cal" style="width:62px;height:62px">0,000<span>CAL</span></div></div>
  <div class="deal-title" style="left:91px;top:630px">HOUSE PARTY</div>
  <div class="deal-text" style="left:91px;top:659px;line-height:26px">20 tenders, 60 wings,<br>sauces, dressings,<br>2 party salads,<br>2 party sides,<br>2 2L</div>
  <div class="price" style="left:234px;top:765px"><sup>$</sup>155.99</div>

  <div class="rule-red" style="left:351px;top:331px;width:2px;height:432px"></div>

  <!-- per person deals -->
  <div class="tab" style="left:361px;top:331px;width:70px;height:114px"><div class="tab-top">1 PAX</div><div class="cal" style="width:62px;height:62px">000<span>CAL</span></div></div>
  <div class="deal-title" style="left:443px;top:342px">SNACK</div>
  <div class="deal-text" style="left:443px;top:372px">2 tenders, sauce,<br>dressing, 1 reg side</div>
  <div class="price" style="left:598px;top:438px"><sup>$</sup>7.00</div>

  <div class="tab" style="left:361px;top:469px;width:70px;height:118px"><div class="tab-top">1 PAX</div><div class="cal" style="width:62px;height:62px">000<span>CAL</span></div></div>
  <div class="deal-title" style="left:443px;top:486px">PARTY</div>
  <div class="deal-text" style="left:443px;top:513px;line-height:23px">2 tenders, 3 wings,<br>sauce, dressing,<br><span style="padding-left:65px">1 reg side</span></div>
  <div class="cup" style="left:442px;top:562px;width:53px;height:49px" role="img" aria-label="12oz soft drink cup"></div>
  <div class="cup-size" style="left:508px;top:585px">12oz</div>
  <div class="price" style="left:594px;top:582px"><sup>$</sup>11.00</div>

  <div class="tab" style="left:361px;top:613px;width:70px;height:120px"><div class="tab-top">1 PAX</div><div class="cal" style="width:62px;height:62px">000<span>CAL</span></div></div>
  <div class="deal-title" style="left:443px;top:630px">FEAST</div>
  <div class="deal-text" style="left:443px;top:657px;line-height:23px">2 tenders, 6 wings,<br>sauce, dressing,<br>1 reg side</div>
  <div class="cup" style="left:442px;top:730px;width:53px;height:70px" role="img" aria-label="20oz soft drink cup"></div>
  <div class="cup-size" style="left:508px;top:765px">20oz</div>
  <div class="price" style="left:591px;top:726px"><sup>$</sup>15.00</div>

  <!-- a la carte grid lines -->
  <div class="rule-slate" style="left:955px;top:59px;width:2px;height:513px"></div>
  <div class="rule-slate" style="left:714px;top:207px;width:479px;height:2px"></div>
  <div class="rule-slate" style="left:714px;top:330px;width:434px;height:2px"></div>
  <div class="rule-slate" style="left:714px;top:468px;width:434px;height:2px"></div>

  <!-- wings -->
  <div class="tab" style="left:716px;top:59px;width:62px;height:144px"><div class="tab-top" style="font-size:15px;margin-top:16px;line-height:20px">+50<br>75,<br>100</div><div class="cal" style="width:56px;height:56px;font-size:13px">000<span>CAL</span></div></div>
  <div class="item-title" style="left:787px;top:74px">WINGS</div>
  <div class="photo" style="left:880px;top:70px;width:50px;height:100px;border-radius:40% 40% 30% 30%;background:radial-gradient(circle,#e0571f,#b5381a)" role="img" aria-label="Sauced chicken wing"></div>
  <div class="item-price" style="left:858px;top:186px;width:68px"><sup>$</sup>0.00</div>

  <!-- tenders -->
  <div class="tab" style="left:968px;top:59px;width:62px;height:144px"><div class="tab-top" style="font-size:15px;margin-top:16px;line-height:20px">+30<br>55,<br>60</div><div class="cal" style="width:56px;height:56px;font-size:13px">000<span>CAL</span></div></div>
  <div class="item-title" style="left:1039px;top:74px">TENDERS</div>
  <div class="photo" style="left:1076px;top:104px;width:98px;height:74px;border-radius:40%;background:radial-gradient(circle,#d17a3a,#a84f23)" role="img" aria-label="Breaded chicken tender"></div>
  <div class="item-price" style="left:1108px;top:186px;width:70px"><sup>$</sup>0.00</div>

  <!-- waffle fries -->
  <div class="tab" style="left:716px;top:208px;width:62px;height:88px"><div class="cal" style="width:56px;height:56px;font-size:13px">000<span>CAL</span></div></div>
  <div class="item-title" style="left:787px;top:215px">WAFFLE<br>FRIES</div>
  <div class="photo" style="left:872px;top:240px;width:64px;height:58px;border-radius:50%;background:radial-gradient(circle,#f29b3e,#d46d22)" role="img" aria-label="Waffle fries"></div>
  <div class="size" style="left:720px;top:305px">PARTY SIZE</div>
  <div class="item-price" style="left:840px;top:304px;width:86px"><sup>$</sup>13.99</div>

  <!-- garlic parm tots -->
  <div class="tab" style="left:968px;top:208px;width:62px;height:88px"><div class="cal" style="width:56px;height:56px;font-size:13px">000<span>CAL</span></div></div>
  <div class="item-title" style="left:1039px;top:215px">GARLIC<br>PARM<br>TOTS</div>
  <div class="size" style="left:972px;top:305px">PARTY SIZE</div>
  <div class="item-price" style="left:1090px;top:304px;width:86px"><sup>$</sup>13.99</div>

  <!-- chicken caesar salad -->
  <div class="tab" style="left:716px;top:331px;width:62px;height:90px"><div class="cal" style="width:56px;height:56px;font-size:13px">000<span>CAL</span></div></div>
  <div class="item-title" style="left:787px;top:340px">CHICKEN<br>CAESAR<br>SALAD</div>
  <div class="photo" style="left:882px;top:394px;width:48px;height:44px;border-radius:50%;background:radial-gradient(circle,#b7c56a,#6f8f3a 70%,#d9d9d9)" role="img" aria-label="Chicken caesar salad bowl"></div>
  <div class="size" style="left:720px;top:443px">PARTY SIZE</div>
  <div class="item-price" style="left:840px;top:442px;width:86px"><sup>$</sup>38.99</div>

  <!-- caesar salad -->
  <div class="tab" style="left:968px;top:331px;width:62px;height:90px"><div class="cal" style="width:56px;height:56px;font-size:13px">000<span>CAL</span></div></div>
  <div class="item-title" style="left:1039px;top:340px">CAESAR<br>SALAD</div>
  <div class="photo" style="left:1104px;top:391px;width:56px;height:46px;border-radius:50%;background:radial-gradient(circle,#b7c56a,#6f8f3a 70%,#d9d9d9)" role="img" aria-label="Caesar salad bowl"></div>
  <div class="size" style="left:972px;top:443px">PARTY SIZE</div>
  <div class="item-price" style="left:1090px;top:442px;width:86px"><sup>$</sup>27.99</div>

  <!-- any sauce -->
  <div class="tab" style="left:716px;top:469px;width:62px;height:90px"><div class="tab-top" style="font-size:16px;margin-top:8px">8oz</div><div class="cal" style="width:56px;height:56px;font-size:13px">000<span>CAL</span></div></div>
  <div class="item-title" style="left:787px;top:478px">ANY<br>SAUCE</div>
  <div class="photo" style="left:790px;top:523px;width:46px;height:45px;border-radius:50%;background:radial-gradient(circle,#4a1410,#2a0a08 70%,#e5e5e5 72%)" role="img" aria-label="Cup of dark dipping sauce"></div>
  <div class="item-price" style="left:846px;top:545px;width:80px"><sup>$</sup>1.99</div>

  <!-- cheese sauce -->
  <div class="tab" style="left:968px;top:469px;width:62px;height:90px"><div class="tab-top" style="font-size:16px;margin-top:8px">8oz</div><div class="cal" style="width:56px;height:56px;font-size:13px">000<span>CAL</span></div></div>
  <div class="item-title" style="left:1039px;top:478px">CHEESE<br>SAUCE</div>
  <div class="photo" style="left:1040px;top:523px;width:46px;height:45px;border-radius:50%;background:radial-gradient(circle,#f2d98a,#e2c46a 70%,#e5e5e5 72%)" role="img" aria-label="Cup of cheese sauce"></div>
  <div class="item-price" style="left:1096px;top:545px;width:80px"><sup>$</sup>2.49</div>

  <!-- flavors -->
  <table class="flavors">
    <thead><tr><th style="width:93px">FLAVOR</th><th style="width:83px">BBQ</th><th style="width:107px">DRY RUBS</th><th style="width:96px">TERIKAYI</th><th>BUFFALO</th></tr></thead>
    <tbody>
      <tr><td>Honey<br>Mustard</td><td>Cajun<br>BBQ</td><td>7 Pepper</td><td>Cajun<br>Terijaki</td><td>Wimpi</td></tr>
      <tr class="hl"><td>Hot Lemon<br>Pepper</td><td>Citrus<br>Chipotle</td><td>Cajun</td><td>Spicy<br>Terijaki</td><td>Cruisin<br>Altitiude</td></tr>
      <tr><td>Jamaican<br>Jerk</td><td>Golden<br>BBQ</td><td>Garlic<br>Parm</td><td>Traditional<br>Terijaki</td><td>Red<br>Alert</td></tr>
      <tr class="hl"><td>Mango<br>Habanero</td><td>Honey<br>BBQ</td><td>Lemon<br>Pepper</td><td></td><td>Jet<br>Fuel</td></tr>
      <tr><td>Sweet<br>Chilli</td><td>Kickin<br>BBQ</td><td>West Texas<br>Mesquite</td><td></td><td>After<br>Burner</td></tr>
    </tbody>
  </table>
</main>
</body>
</html>
```